Pet business needs a business card

Pet shop needs a business card. Like dark background and and debased look.

Hedgerowpups
Lindelaan 27
B - 3270 Korbeek
Belgium

www.hedgerowpups.example
mail@hedgerowpups.example
Phone +32471869203

I will ad a tagline shortly.

Industry/Entity Type

Shop

Font styles to use
Sans Serif

Requirements
Must have
• Must be possible to print the card debased. See example image.

```html
<!DOCTYPE html>
<html lang="en">
<head>
<meta charset="utf-8">
<title>Hedgerowpups – Name Card</title>
<link rel="stylesheet" href="https://fonts.googleapis.com/css2?family=Arimo:wght@400;700&display=swap">
<style>
  :root{
    --sheet-light:#e4e5e8;
    --sheet-dark:#a9abaf;
    --card:#2d3039;
    --card-edge:#4a4c52;
    --shadow:#6c6e73;
    --orange:#f7a33d;
    --ink:#45474d;
    --label:#3f4044;
    --pattern-b:#5b5d63;
  }
  *{margin:0;padding:0;box-sizing:border-box}
  html,body{width:1200px;height:846px;overflow:hidden}
  body{
    position:relative;
    font-family:"Arimo",Arial,sans-serif;
    background:linear-gradient(100deg,var(--sheet-light) 0%,#c9cacd 45%,var(--sheet-dark) 75%,#c2c3c6 100%);
  }
  .side-label{
    position:absolute;top:38px;font-size:22px;font-weight:700;color:var(--label);
    transform:translateX(-50%);
  }
  .sheet-title{
    position:absolute;left:610px;top:785px;transform:translateX(-50%);
    font-size:46px;font-weight:700;color:var(--label);letter-spacing:-1px;
  }
  .card{
    position:absolute;width:566px;height:306px;border-radius:14px;
    background:var(--card);overflow:hidden;
    box-shadow:8px 7px 0 var(--shadow);
  }
  .card svg{position:absolute;inset:0;width:100%;height:100%}
  .card-front-a{left:26px;top:75px}
  .card-back-a{left:621px;top:75px}
  .card-front-b{left:24px;top:451px}
  .card-back-b{left:618px;top:451px}
  .brand{
    position:absolute;display:flex;align-items:center;gap:8px;
    font-weight:700;color:var(--orange);letter-spacing:.5px;white-space:nowrap;
  }
  .brand-dot{display:block;border-radius:50%;background:var(--orange)}
  .address{
    position:absolute;font-size:10px;font-weight:700;line-height:14px;color:var(--ink);white-space:nowrap;
  }
  .contact{
    position:absolute;font-size:8px;line-height:12px;color:var(--ink);white-space:nowrap;
    display:grid;grid-template-columns:30px 8px auto;
  }
</style>
</head>
<body>
  <div class="side-label" style="left:298px">Front</div>
  <div class="side-label" style="left:956px">Back</div>

  <!-- Version A, front -->
  <div class="card card-front-a">
    <svg viewBox="0 0 566 306" aria-hidden="true">
      <rect x="0" y="148" width="11" height="96" fill="var(--card-edge)"/>
      <path d="M11 148 H370 Q395 148 395 130 L410 150 Q388 162 392 190 Q398 226 340 229 L318 229 V244 H11 Z" fill="var(--orange)"/>
      <circle cx="414" cy="125" r="33" fill="var(--orange)"/>
      <rect x="318" y="229" width="194" height="55" rx="22" fill="var(--orange)"/>
      <rect x="318" y="229" width="40" height="30" fill="var(--orange)"/>
    </svg>
    <div class="brand" style="left:72px;top:100px;font-size:22px">hedgerowpups<span class="brand-dot" style="width:10px;height:10px"></span></div>
    <div class="address" style="left:16px;top:178px">Hedgerowpups<br>Lindelaan 27<br>B - 3270 Korbeek<br>Belgia</div>
    <div class="contact" style="left:336px;top:239px">
      <span>Web</span><span>:</span><span>www.hedgerowpups.example</span>
      <span>MAIL</span><span>:</span><span>mail@hedgerowpups.example</span>
      <span>PHONE:</span><span></span><span>+32471869203</span>
    </div>
  </div>

  <!-- Version A, back -->
  <div class="card card-back-a">
    <svg viewBox="0 0 566 306" aria-hidden="true">
      <rect x="551" y="148" width="15" height="96" fill="var(--card-edge)"/>
      <circle cx="448" cy="120" r="33" fill="var(--orange)"/>
      <path d="M448 150 Q432 168 452 186 Q478 210 470 228 H551 V148 H470 Q455 148 448 150 Z" fill="var(--orange)"/>
      <rect x="365" y="228" width="186" height="56" rx="22" fill="var(--orange)"/>
      <rect x="520" y="228" width="31" height="56" fill="var(--orange)"/>
    </svg>
    <div class="brand" style="left:186px;top:182px;font-size:22px">hedgerowpups<span class="brand-dot" style="width:10px;height:10px"></span></div>
  </div>

  <!-- Version B, front -->
  <div class="card card-front-b">
    <svg viewBox="0 0 566 306" aria-hidden="true">
      <polygon points="286,306 544,0 566,0 566,306" fill="var(--pattern-b)" role="img" aria-label="Diagonal band of overlapping grey circles pattern"/>
      <path d="M0 148 H170 L118 244 H0 Z" fill="var(--orange)"/>
      <path d="M182 148 H306 L328 162 V236 Q328 244 320 244 H131 Z" fill="var(--orange)"/>
    </svg>
    <div class="brand" style="left:72px;top:104px;font-size:22px">hedgerowpups<span class="brand-dot" style="width:10px;height:10px"></span></div>
    <div class="address" style="left:10px;top:175px">Hedgerowpups<br>Lindelaan 27<br>B - 3270 Korbeek<br>Belgia</div>
    <div class="contact" style="left:176px;top:202px">
      <span>Web</span><span>:</span><span>www.hedgerowpups.example</span>
      <span>MAIL</span><span>:</span><span>mail@hedgerowpups.example</span>
      <span>PHONE:</span><span></span><span>+32471869203</span>
    </div>
  </div>

  <!-- Version B, back -->
  <div class="card card-back-b">
    <svg viewBox="0 0 567 306" aria-hidden="true">
      <polygon points="0,0 284,0 0,273" fill="var(--pattern-b)" role="img" aria-label="Corner of overlapping grey circles pattern"/>
      <polygon points="286,306 546,0 567,0 567,306" fill="var(--pattern-b)" role="img" aria-label="Diagonal band of overlapping grey circles pattern"/>
    </svg>
    <div class="brand" style="left:236px;top:168px;font-size:17px">hedgerowpups<span class="brand-dot" style="width:8px;height:8px"></span></div>
  </div>

  <div class="sheet-title">NameCard</div>
</body>
</html>
```